"Eyebrow Threading Flyer Design"

We need a flyer design for a new service that will be provided in our established Beauty Salon in Toorak called "Threading". We provide all beauty services for our clients & would like to now introduce this very popular ancient method of hair removal.
Following are four "40% Off Threading Combo Packages" that will hopefully tempt new clients into our salon.
#Package 1- Eyebrow Threading plus Eyebrow Tint or Eyelash Tint Normally $53 Now $32
#Package 2- Eyebrow Threading plus Full Set Mink Lash Extensions
Normally $208 Now $125
#Package 3- Eyebrow Threading plus Glossine Manicure Or Pedicure
Normally $128 Now $77
#Package 4- Eyebrow Threading plus Collagen Facial
Normally $148 Now $89
We would like to see designs that use pink with whit or black to suit logo & business name & final design should be girly/feminine 7 fun.
On the back we would like the following details:
Velvet Daisy Beauty, "Marlowe Court", shop 7, 846 Brindle Street, 3917
Tel: 03 9471 3629, Email: info@velvetdaisybeauty.example, Web: www.velvetdaisybeauty.example
A map of exact location and business hours:
Mon 9am to 5pm, Tue 9am to 6pm, Wed 9am to 6pm, Thu 9am to 8pm, Fri 9am to 6pm, sat 9am to 5pm

Target Market(s)

Women between the ages of 20 to 60 years of age

Industry/Entity Type

Hair

Font styles to use
Script

Colors
e34297
000000

Requirements
Must have
• Pink and black or pink and white colors
Should not have
• Fake looking eyelashes displayed

```html
<!DOCTYPE html>
<html lang="en">
<head>
<meta charset="utf-8">
<title>Threading Packages Flyer</title>
<link href="https://fonts.googleapis.com/css2?family=Roboto+Condensed:wght@400;700&family=Roboto:wght@300&family=Kaushan+Script&display=swap" rel="stylesheet">
<style>
  :root{
    --backdrop:#e7e6e3;
    --pink:#d81f55;
    --pink-deep:#c4164a;
    --ink:#2a2a2a;
    --ink-soft:#444;
    --white:#ffffff;
    --pill-light:#f4f4f4;
    --price-red:#c8102e;
    --price-pink:#f26b9c;
    --divider:#b9b9b9;
  }
  *{box-sizing:border-box;margin:0;padding:0}
  html,body{width:1200px;height:1148px;overflow:hidden;background:var(--backdrop)}
  .flyer{
    position:absolute;left:220px;top:44px;width:760px;height:1060px;
    background:linear-gradient(180deg,var(--pink) 0%,var(--pink) 36%,var(--pink-deep) 100%);
    font-family:"Roboto Condensed",Arial,sans-serif;overflow:hidden;
  }
  .ribbon{position:absolute;left:185px;top:44px;width:390px;height:66px}
  .ribbon-text{
    position:absolute;left:0;top:0;width:390px;height:56px;
    display:flex;align-items:center;justify-content:center;
    color:var(--pink-deep);font-weight:700;font-size:36px;letter-spacing:.5px;
  }
  .headline{position:absolute;left:0;width:760px;text-align:center;color:var(--white)}
  .headline-top{top:138px;font-weight:700;font-size:32px;text-shadow:0 2px 3px rgba(0,0,0,.25)}
  .headline-main{top:180px;font-family:"Roboto",Arial,sans-serif;font-weight:300;font-size:50px;letter-spacing:1px}
  .photo-strip{position:absolute;left:0;top:260px;width:760px;height:140px;display:flex;gap:4px;background:var(--white);padding:0 0}
  .photo{flex:1;height:140px}
  .photo-facial{background:linear-gradient(135deg,#f1e6de,#7a4a30 60%,#e9e0d6)}
  .photo-threading{background:linear-gradient(135deg,#e9c3a8,#d9a88a 55%,#c48b6c)}
  .photo-pedicure{background:linear-gradient(135deg,#5a3520,#a86a45 50%,#f0d8c0)}
  .photo-makeup{background:linear-gradient(135deg,#f5f0ee,#dcb39a 55%,#f3ece8)}
  .packages{position:absolute;left:0;top:0;width:760px;height:1060px}
  .pill{
    position:absolute;left:130px;width:510px;height:128px;border-radius:64px;
    display:flex;align-items:center;padding:0 34px;
  }
  .pill-light{background:linear-gradient(180deg,#ffffff,#e9e9e9);box-shadow:0 8px 12px rgba(0,0,0,.35);z-index:2}
  .pill-dark{background:linear-gradient(180deg,#3a3a3a,#232323);height:140px;z-index:1;color:var(--white)}
  .pkg-1{top:415px}
  .pkg-2{top:540px;left:140px}
  .pkg-3{top:678px;left:140px}
  .pkg-4{top:805px;left:150px}
  .col{display:flex;flex-direction:column;justify-content:center;text-align:center;height:84px}
  .col-number{width:96px}
  .col-service{flex:1;border-left:1px solid var(--divider);border-right:1px solid var(--divider);padding:0 12px}
  .col-price{width:120px}
  .pkg-label{font-weight:700;font-size:21px;color:var(--ink-soft)}
  .pkg-num{font-weight:700;font-size:62px;line-height:58px;color:var(--ink)}
  .pill-dark .pkg-label{color:#d9d9d9}
  .pill-dark .pkg-num{color:#e6e6e6}
  .service{font-weight:700;font-size:17px;line-height:19px;color:var(--ink-soft);text-transform:uppercase}
  .pill-dark .service{color:var(--white)}
  .plus{font-family:"Kaushan Script",cursive;font-size:22px;line-height:26px;color:var(--price-red)}
  .pill-dark .plus{color:var(--price-pink)}
  .normally{font-size:14px;color:var(--ink-soft)}
  .pill-dark .normally{color:#ddd}
  .was{font-weight:700;font-size:23px;color:#666;text-decoration:line-through;text-decoration-color:var(--price-red)}
  .pill-dark .was{color:#ddd}
  .now{font-size:15px;color:var(--ink-soft)}
  .pill-dark .now{color:#ddd}
  .now strong{font-size:30px;color:var(--price-red)}
  .pill-dark .now strong{color:var(--price-pink)}
  .tail{position:absolute;right:-6px;bottom:-36px;width:70px;height:60px}
</style>
</head>
<body>
<main class="flyer">
  <svg class="ribbon" viewBox="0 0 390 66" aria-hidden="true">
    <polygon points="0,14 30,14 30,62 12,62 22,38" fill="#bdbdbd"/>
    <polygon points="390,14 360,14 360,62 378,62 368,38" fill="#bdbdbd"/>
    <rect x="22" y="0" width="346" height="56" fill="#f7f7f7"/>
  </svg>
  <div class="ribbon-text" style="left:185px;top:44px">NOW INTRODUCING</div>

  <h1 class="headline headline-top">VERY POPULAR ANCIENT METHOD OF</h1>
  <h2 class="headline headline-main">HAIR REMOVAL</h2>

  <div class="photo-strip">
    <div class="photo photo-facial" role="img" aria-label="Photo of a relaxing facial mask treatment"></div>
    <div class="photo photo-threading" role="img" aria-label="Photo of eyebrow threading"></div>
    <div class="photo photo-pedicure" role="img" aria-label="Photo of a pedicure foot soak with flowers"></div>
    <div class="photo photo-makeup" role="img" aria-label="Photo of makeup being applied"></div>
  </div>

  <section class="packages">
    <div class="pill pill-light pkg-1">
      <div class="col col-number"><span class="pkg-label">PACKAGE</span><span class="pkg-num">#1</span></div>
      <div class="col col-service"><span class="service">Eyebrow Threading</span><span class="plus">Plus!</span><span class="service">Eyebrow Tint or<br>Eyelash Tint</span></div>
      <div class="col col-price"><span class="normally">NORMALLY</span><span class="was">$53</span><span class="now">NOW <strong>$32</strong></span></div>
    </div>

    <div class="pill pill-dark pkg-2">
      <div class="col col-price"><span class="normally">NORMALLY</span><span class="was">$208</span><span class="now">NOW <strong>$125</strong></span></div>
      <div class="col col-service"><span class="service">Eyebrow Threading</span><span class="plus">Plus!</span><span class="service">Full Set Mink<br>Lash Extensions</span></div>
      <div class="col col-number"><span class="pkg-label">PACKAGE</span><span class="pkg-num">#2</span></div>
    </div>

    <div class="pill pill-light pkg-3">
      <div class="col col-number"><span class="pkg-label">PACKAGE</span><span class="pkg-num">#3</span></div>
      <div class="col col-service"><span class="service">Eyebrow Threading</span><span class="plus">Plus!</span><span class="service">Glossine Manicure<br>or Pedicure</span></div>
      <div class="col col-price"><span class="normally">NORMALLY</span><span class="was">$128</span><span class="now">NOW <strong>$77</strong></span></div>
    </div>

    <div class="pill pill-dark pkg-4">
      <div class="col col-price"><span class="normally">NORMALLY</span><span class="was">$148</span><span class="now">NOW <strong>$89</strong></span></div>
      <div class="col col-service"><span class="service">Eyebrow Threading</span><span class="plus">Plus!</span><span class="service">Collagen Facial</span></div>
      <div class="col col-number"><span class="pkg-label">PACKAGE</span><span class="pkg-num">#4</span></div>
      <svg class="tail" viewBox="0 0 70 60" aria-hidden="true">
        <path d="M0,0 L60,0 Q66,30 70,60 Q40,44 10,30 Z" fill="#232323"/>
      </svg>
    </div>
  </section>
</main>
</body>
</html>
```